Signboard menu for a Fastfood takeaway shop

My current signboard menu is old now, I want to upgrade to a new, bigger and brighter signboard menu.
Photos of the old menu attached but there are some changes in each sections of the menu needs to be changed.
Size of the signboard :
L: 1700cm
H: 1200cm

Industry/Entity Type

Fastfood Hospitality

Colors
FFC000
F8CF3A
FAE287
FDF2CF
FEFAEE

```html
<!DOCTYPE html>
<html lang="en">
<head>
<meta charset="utf-8">
<title>Takeaway Menu Board</title>
<link rel="stylesheet" href="https://fonts.googleapis.com/css2?family=Dancing+Script:wght@700&family=Pathway+Gothic+One&display=swap">
<style>
:root{
  --board-yellow:#F6D325;
  --brand-red:#E3141E;
  --ink:#1b1712;
  --white:#ffffff;
  --gold:#FFC000;
  --cream:#FDF2CF;
}
*{margin:0;padding:0;box-sizing:border-box}
html,body{width:1200px;height:848px;overflow:hidden;background:var(--white)}
.menu-board{position:relative;width:1200px;height:848px;font-family:"Pathway Gothic One",sans-serif;color:var(--ink)}
.panel{position:absolute;left:51px;top:37px;width:1098px;height:775px;background:var(--board-yellow)}
.heading{position:absolute;background:var(--brand-red);color:var(--white);border-radius:12px;font-family:"Dancing Script",cursive;font-weight:700;font-size:29px;line-height:38px;padding-left:12px;white-space:nowrap}
.heading.two-line{font-size:28px;line-height:27px;padding-top:5px}
.art{position:absolute;border-radius:40%}
.line{position:absolute;height:27px;line-height:27px;font-size:22px;letter-spacing:-0.4px;display:flex;justify-content:space-between;white-space:nowrap}
.line.tight{font-size:21px;letter-spacing:-0.8px}
.note{position:absolute;height:20px;line-height:20px;font-size:17px;letter-spacing:-0.6px;white-space:nowrap}
.small{font-size:16px;letter-spacing:-0.4px}
.col-burgers{left:77px;width:239px}
.col-rolls{left:345px;width:240px}
.col-hot{left:613px;width:244px}
.col-extras{left:882px;width:234px}
.col-extras-wide{left:882px;width:262px}
.col-pack{left:882px;width:241px}
.grid-hot{display:grid;grid-template-columns:80px 36px 1fr auto}
.grid-sand{display:grid;grid-template-columns:80px 52px 1fr auto}
.grid-extra{display:grid;grid-template-columns:80px 50px 1fr auto}
.grid-hot .name2{padding-left:12px}
.span3{grid-column:1 / 4}
.span-mid{grid-column:2 / 4}
.extra-price{display:flex;align-items:baseline;gap:8px}
.brekky{position:absolute;left:600px;top:651px;width:265px;height:130px;background:var(--brand-red);border-radius:12px;color:var(--white)}
.brekky-title{position:absolute;left:13px;top:2px;font-family:"Dancing Script",cursive;font-weight:700;font-size:27px;line-height:36px;color:var(--gold);white-space:nowrap}
.brekky .line{left:13px;width:240px;font-size:19px}
.brekky .price{font-size:22px}
</style>
</head>
<body>
<main class="menu-board">
  <div class="panel"></div>

  <!-- Burgers -->
  <h2 class="heading" style="left:63px;top:55px;width:114px">Burgers</h2>
  <div class="art" role="img" aria-label="Illustration of a cheeseburger" style="left:199px;top:57px;width:73px;height:57px;background:radial-gradient(circle,#c8782a,#e39a3c 60%,#6aa53a)"></div>
  <div class="note col-burgers" style="top:98px">Beef or Chicken</div>
  <div class="line col-burgers" style="top:120px"><span>Plain</span><span>7.00</span></div>
  <div class="line col-burgers" style="top:147px"><span>Works</span><span>10.00</span></div>
  <div class="line col-burgers" style="top:174px"><span>Cheese</span><span>8.00</span></div>
  <div class="line col-burgers" style="top:201px"><span>Mega</span><span>15.00</span></div>
  <div class="note col-burgers" style="top:226px">Works Burger with double meat, double bacon &amp; egg</div>
  <div class="line col-burgers" style="top:250px"><span>Schnitzel burgers</span><span class="extra-price"><span class="small">extra</span>1.50</span></div>
  <div class="line col-burgers" style="top:277px"><span>Bacon/Cheese</span><span>9.00</span></div>
  <div class="line col-burgers" style="top:304px"><span>Hawaiian</span><span>11.00</span></div>
  <div class="note col-burgers" style="top:329px">Works burger with Pineapple</div>
  <div class="line col-burgers" style="top:351px"><span>Bacon/Egg</span><span>9.50</span></div>
  <div class="line col-burgers" style="top:378px"><span>Mexican</span><span>8.00</span></div>

  <!-- Kebabs -->
  <h2 class="heading" style="left:63px;top:427px;width:99px">Kebabs</h2>
  <div class="art" role="img" aria-label="Illustration of a kebab wrap with salad" style="left:172px;top:422px;width:102px;height:48px;background:radial-gradient(ellipse,#c7844a,#e9cfa0 55%,#5aa23a)"></div>
  <div class="line col-burgers" style="top:463px"><span>Chicken</span><span>12.50</span></div>
  <div class="line col-burgers" style="top:490px"><span>Lamb</span><span>14.50</span></div>
  <div class="line col-burgers" style="top:517px"><span>Mix</span><span>14.50</span></div>

  <!-- Bacon & Egg -->
  <h2 class="heading two-line" style="left:63px;top:569px;width:199px;height:65px">Bacon &amp; Egg<br>Rolls or Wraps</h2>
  <div class="art" role="img" aria-label="Illustration of a bacon and egg roll" style="left:264px;top:588px;width:68px;height:42px;background:radial-gradient(circle,#f7d23a,#d98a3a 50%,#a2412c)"></div>
  <div class="line col-burgers" style="top:640px"><span>Bacon/Egg</span><span>7.00</span></div>
  <div class="line col-burgers" style="top:667px"><span>Bacon/Egg/Cheese</span><span>8.20</span></div>
  <div class="line col-burgers" style="top:694px"><span>Bacon/Egg/Cheese/Onion</span><span>9.20</span></div>
  <div class="line col-burgers" style="top:721px"><span>Wraps</span><span class="extra-price"><span class="small">extra</span>3.00</span></div>

  <!-- Gravy Rolls -->
  <h2 class="heading" style="left:332px;top:55px;width:145px">Gravy Rolls</h2>
  <div class="art" role="img" aria-label="Illustration of roast meat and bread roll" style="left:480px;top:51px;width:98px;height:43px;background:radial-gradient(ellipse,#d9896a,#a44a30 60%,#e0a55a)"></div>
  <div class="line col-rolls" style="top:96px"><span>Slow cook Beef</span><span>8.50</span></div>
  <div class="line col-rolls" style="top:123px"><span>Slow cook Pork</span><span>8.00</span></div>
  <div class="line col-rolls" style="top:151px"><span>Rissole</span><span>8.00</span></div>
  <div class="line col-rolls" style="top:178px"><span>Sausage</span><span>7.00</span></div>
  <div class="line col-rolls" style="top:205px"><span>Schnitzel</span><span>8.00</span></div>
  <div class="line col-rolls" style="top:232px"><span>Chips</span><span>6.50</span></div>

  <!-- Schnitzel Wraps -->
  <h2 class="heading" style="left:332px;top:261px;width:194px">Schnitzel Wraps</h2>
  <div class="art" role="img" aria-label="Illustration of a schnitzel wrap with salad" style="left:530px;top:256px;width:71px;height:46px;background:radial-gradient(ellipse,#e9d3a8,#d9503a 50%,#5aa23a)"></div>
  <div class="line col-rolls" style="top:302px"><span>Caesar</span><span>12.00</span></div>
  <div class="line col-rolls" style="top:329px"><span>Salad and Cheese</span><span>11.00</span></div>
  <div class="line col-rolls" style="top:357px"><span>Works</span><span>14.50</span></div>
  <div class="note col-rolls" style="top:379px">with Bacon, Egg, Cheese and all salad</div>
  <div class="line col-rolls" style="top:407px"><span>Mexican</span><span>10.50</span></div>
  <div class="note col-rolls" style="top:433px">Mexican spiced Schnitzel with Lettuce, Tomato,</div>
  <div class="note col-rolls" style="top:452px">Spanish onion, Cheese, Sour Cream and Hot chilli sauce</div>
  <div class="line col-rolls" style="top:479px"><span>Hawaiian</span><span>12.00</span></div>
  <div class="note col-rolls" style="top:505px">with Bacon, Lettuce, Tomato, Pineapple,</div>
  <div class="note col-rolls" style="top:524px">Cheese with Honey mustard</div>

  <!-- Snack Packs -->
  <h2 class="heading" style="left:332px;top:548px;width:155px">Snack Packs</h2>
  <div class="note col-rolls" style="top:585px">Kebab meats with Chips, Spanish Onions, Cheese</div>
  <div class="note col-rolls" style="top:603px">and Sauce of your choice</div>
  <div class="line col-rolls" style="top:626px"><span>Chicken</span><span>13.00</span></div>
  <div class="line col-rolls" style="top:651px"><span>Lamb</span><span>15.00</span></div>
  <div class="line col-rolls" style="top:675px"><span>Mix</span><span>15.00</span></div>

  <!-- Salad in Tubs -->
  <h2 class="heading" style="left:332px;top:704px;width:169px">Salad in Tubs</h2>
  <div class="line col-rolls" style="top:739px"><span>Plain Salad</span><span>7.50</span></div>
  <div class="line col-rolls" style="top:763px"><span>Caesar Salad</span><span>10.00</span></div>

  <!-- Hot Food -->
  <h2 class="heading" style="left:600px;top:55px;width:119px">Hot Food</h2>
  <div class="art" role="img" aria-label="Illustration of a grilled sausage" style="left:745px;top:57px;width:80px;height:32px;background:linear-gradient(180deg,#f05a3a,#c8201e)"></div>
  <div class="line col-hot grid-hot" style="top:94px"><span>Scallops</span><span>2.00</span><span class="name2">Dim Sim</span><span>2.00</span></div>
  <div class="line col-hot grid-hot" style="top:121px"><span>Hash Brown</span><span>2.50</span><span class="name2">Sausage</span><span>3.00</span></div>
  <div class="line col-hot grid-hot" style="top:148px"><span>Corn jack</span><span>2.50</span><span>Chicken Stick</span><span>3.70</span></div>
  <div class="line col-hot grid-hot" style="top:175px"><span>Chook Roll</span><span>3.50</span><span class="name2">Spring Roll</span><span>3.50</span></div>
  <div class="line col-hot grid-hot" style="top:202px"><span>Battered Sav</span><span>3.50</span><span class="name2">Corny Pup</span><span>4.50</span></div>
  <div class="line col-hot grid-hot" style="top:230px"><span class="span3">Mini Chicken Dim Sim <span class="small">x 6</span></span><span>3.00</span></div>
  <div class="line col-hot grid-hot" style="top:257px"><span>Chips</span><span class="span-mid">Small</span><span>4.00</span></div>
  <div class="art" role="img" aria-label="Illustration of a carton of chips" style="left:630px;top:285px;width:49px;height:50px;border-radius:6px;background:linear-gradient(180deg,#f4c43a,#e0892a)"></div>
  <div class="line col-hot grid-hot" style="top:284px"><span></span><span class="span-mid">Medium</span><span>6.00</span></div>
  <div class="line col-hot grid-hot" style="top:311px"><span></span><span class="span-mid">Large</span><span>8.00</span></div>
  <div class="line col-hot" style="top:338px"><span>Add Gravy</span><span>2.00</span></div>

  <!-- Sandwiches -->
  <h2 class="heading" style="left:600px;top:383px;width:153px">Sandwiches</h2>
  <div class="art" role="img" aria-label="Illustration of a sandwich" style="left:767px;top:378px;width:72px;height:38px;background:linear-gradient(180deg,#f3dca8,#5aa23a 50%,#e05a3a)"></div>
  <div class="line col-hot grid-sand" style="top:420px"><span>Vegespread</span><span>4.60</span><span>Cheese</span><span>4.50</span></div>
  <div class="line col-hot grid-sand" style="top:443px"><span>Tomato</span><span>4.50</span><span>Salad</span><span>7.00</span></div>
  <div class="line col-hot grid-sand" style="top:470px"><span>Ham</span><span>7.50</span><span>Chicken</span><span>7.50</span></div>
  <div class="line col-hot grid-sand" style="top:498px"><span>Roast Beef</span><span>7.50</span><span>Rissole</span><span>7.50</span></div>
  <div class="line col-hot grid-sand" style="top:525px"><span>Sausage</span><span>7.00</span><span>Scallop</span><span>6.00</span></div>
  <div class="line col-hot grid-sand" style="top:552px"><span>Chip</span><span>6.00</span><span>Bacon</span><span>7.00</span></div>
  <div class="line col-hot grid-sand" style="top:579px"><span>Bacon/Egg</span><span>7.00</span><span>Schnitzel</span><span>8.50</span></div>
  <div class="line col-hot grid-sand" style="top:606px"><span>Roll</span><span>.50¢</span><span></span><span></span></div>

  <!-- Big Brekky Special -->
  <section class="brekky">
    <h2 class="brekky-title">Big Brekky Special</h2>
    <div class="art" role="img" aria-label="Illustration of a takeaway coffee cup" style="left:230px;top:10px;width:24px;height:34px;border-radius:3px;background:linear-gradient(180deg,#ffffff,#d9a06a)"></div>
    <div class="line" style="top:40px"><span>Bacon, 2x Eggs, Sausage, Fried Tomato,</span></div>
    <div class="line" style="top:66px"><span>Hashbrown and Toast</span><span class="price">15.00</span></div>
    <div class="line" style="top:93px"><span>with a small coffee</span><span class="price">17.00</span></div>
  </section>

  <!-- Extras -->
  <h2 class="heading" style="left:869px;top:57px;width:89px">Extras</h2>
  <div class="line col-extras grid-extra" style="top:94px"><span>Pineapple</span><span>1.00</span><span>Sauce</span><span>.50¢</span></div>
  <div class="line col-extras grid-extra" style="top:121px"><span>Avocado</span><span>1.20</span><span>Cheese</span><span>1.20</span></div>
  <div class="line tight col-extras-wide" style="top:148px"><span>Tomato/Beetroot/Onion/Cucumber</span><span>.50¢</span></div>
  <div class="line col-extras grid-extra" style="top:175px"><span>Bacon/Meat</span><span>2.50</span><span>Egg</span><span>1.50</span></div>
  <div class="line col-extras" style="top:202px"><span>Kebab Meat <span class="small">100g</span></span></div>
  <div class="line col-extras grid-extra" style="top:230px"><span>Chicken</span><span>3.50</span><span>Lamb</span><span>4.50</span></div>

  <!-- Seafood -->
  <h2 class="heading" style="left:869px;top:272px;width:104px">Seafood</h2>
  <div class="art" role="img" aria-label="Illustration of fried fish and chips on a plate" style="left:996px;top:269px;width:89px;height:42px;background:radial-gradient(ellipse,#e8823a,#f4c43a 55%,#4a8fd0)"></div>
  <div class="line col-extras" style="top:308px"><span>Calamari Ring</span><span>2.00</span></div>
  <div class="line col-extras" style="top:336px"><span>Cocktail Fish</span><span>2.50</span></div>
  <div class="line col-extras" style="top:363px"><span>Crab Stick</span><span>2.50</span></div>
  <div class="line col-extras" style="top:390px"><span>Prawn Cutlet</span><span>2.50</span></div>
  <div class="line col-extras" style="top:417px"><span>Fish Cake</span><span>3.50</span></div>
  <div class="line col-extras" style="top:444px"><span>Battered Fish</span><span>7.00</span></div>

  <!-- Seafood pack -->
  <h2 class="heading" style="left:869px;top:488px;width:161px">Seafood pack</h2>
  <div class="art" role="img" aria-label="Illustration of a seafood platter with lobster and lemon" style="left:1043px;top:483px;width:91px;height:45px;background:radial-gradient(ellipse,#e84a2a,#f4a43a 55%,#3f7fc0)"></div>
  <div class="line col-extras" style="top:529px"><span>#1&nbsp; Traditional</span><span>9.00</span></div>
  <div class="note col-pack" style="top:553px">Battered Fish &amp; Chip</div>
  <div class="line col-extras" style="top:580px"><span>#2&nbsp; Snacking Pack</span><span>9.00</span></div>
  <div class="note col-pack" style="top:604px">3 Cocktail Fish &amp; Chip</div>
  <div class="line col-pack" style="top:627px"><span>#3&nbsp; Fisherman Basket</span><span>18.00</span></div>
  <div class="note col-pack" style="top:652px">2 Calamari ring, 2 Prawn cutlet, 1 Crabstick,</div>
  <div class="note col-pack" style="top:671px">1 Cocktail Fish, Chip &amp; 1 can of soft drink</div>
  <div class="line col-pack" style="top:698px"><span>#4&nbsp; Family Feast</span><span>40.00</span></div>
  <div class="note col-pack" style="top:724px">4 Prawn cutlets, 4 Calamari rings, 4 Crabstick,</div>
  <div class="note col-pack" style="top:744px">6 cocktail fish &amp; 1.25l bottle of soft drink</div>
</main>
</body>
</html>
```